Marketing Postcard Design for a Medical Supply Company

We are sending a marketing postcard to healthcare facilities within our state. We are in need of a design for a 6"x9" postcard, front and back with our logo, website www.carevale.shop, phone number 808-241-7739, and 12 products. The products are face shields, nitrile gloves, vinyl gloves, isolation gowns, gallon hand sanitizer, black KN95's, white KN95's, 4520 N95, 4530 N95, biohazard bags, Puratex wipes, and Kor spray. All of these items can be found on our website at carevale.shop. Please include a promo code, 10OFF for 10% Off. The design should be clean, professional, and appeal to a healthcare or medical audience.

```html
<!DOCTYPE html>
<html lang="en">
<head>
<meta charset="UTF-8">
<title>Carevale Medical Supply – Postcard</title>
<link href="https://fonts.googleapis.com/css2?family=Montserrat:wght@400;500;600;700;800&display=swap" rel="stylesheet">
<style>
  :root{
    --green:#1a9a48;
    --green-dark:#1c6a33;
    --ink:#1f1f1f;
    --paper:#ffffff;
    --tile:#f4f5f4;
    --backdrop:#8a8a8a;
    --rule:#9a9a9a;
  }
  *{box-sizing:border-box;margin:0;padding:0}
  html,body{width:1200px;height:900px;overflow:hidden}
  body{background:var(--backdrop);font-family:"Montserrat",sans-serif;color:var(--ink);position:relative}

  .postcard{position:absolute;top:260px;width:570px;height:380px;background:var(--paper);padding:14px;box-shadow:0 4px 14px rgba(0,0,0,.25)}
  .postcard--front{left:20px}
  .postcard--back{left:610px}

  /* ---------- front ---------- */
  .front-frame{width:100%;height:100%;border:1.5px solid var(--green);display:flex;flex-direction:column}
  .front-body{flex:1;display:flex;min-height:0}
  .intro{width:190px;border-right:1.5px solid var(--green);display:flex;flex-direction:column}
  .brand{display:flex;align-items:center;gap:8px;padding:22px 14px 0}
  .brand-dot{width:30px;height:30px;border-radius:50%;background:var(--green);flex:none}
  .brand-name{font-weight:800;color:var(--green);font-size:22px;line-height:1;letter-spacing:.5px}
  .brand-sub{font-weight:800;color:var(--green);font-size:7.5px;letter-spacing:2.6px;margin-top:3px}
  .headline{padding:18px 14px 0;font-weight:800;font-size:19px;line-height:1.1;color:var(--green-dark)}
  .headline span{color:var(--green)}
  .intro-copy{padding:8px 14px 0;font-size:10px;font-weight:600;line-height:1.35}
  .promo{margin-top:auto;display:flex;height:78px}
  .promo-code{flex:1;background:var(--green-dark);color:#fff;display:flex;flex-direction:column;justify-content:center;padding-left:12px;font-size:10px;font-weight:500}
  .promo-code strong{font-size:19px;font-weight:800;letter-spacing:.5px}
  .promo-offer{width:92px;background:var(--green);color:#fff;display:flex;flex-direction:column;justify-content:center;align-items:center;font-weight:800}
  .promo-offer .for{font-size:11px}
  .promo-offer .pct{font-size:30px;line-height:1}
  .promo-offer .off{font-size:13px}

  .product-grid{flex:1;display:grid;grid-template-columns:1fr 1fr;grid-template-rows:repeat(3,1fr)}
  .product-grid--back{grid-template-columns:1fr 1fr}
  .product{border-right:1.5px solid var(--green);border-bottom:1.5px solid var(--green);display:flex;flex-direction:column;min-height:0}
  .product:nth-child(2n){border-right:none}
  .product:nth-last-child(-n+2){border-bottom:none}
  .product-photo{flex:1;margin:6px 22px 4px}
  .product-label{background:var(--green);color:#fff;font-weight:800;font-size:10.5px;text-align:center;padding:4px 0;letter-spacing:.3px}

  .contact-bar{height:26px;background:var(--green-dark);color:#fff;display:flex;align-items:center;gap:22px;padding:0 12px;font-size:10.5px;font-weight:600}
  .contact-item{display:flex;align-items:center;gap:5px}
  .contact-icon{width:13px;height:13px;border-radius:50%;background:var(--green);display:flex;align-items:center;justify-content:center}

  /* photo tones */
  .ph-shield{background:radial-gradient(circle at 50% 45%,#e8eef3,#c9d6e2)}
  .ph-nitrile{background:radial-gradient(circle at 50% 50%,#7cc3ec,#3f8fd0 70%,#f3f6f8 100%)}
  .ph-vinyl{background:linear-gradient(90deg,#f1ece8,#e7d9cf)}
  .ph-gown{background:radial-gradient(circle,#3aa6e6,#1f86cf 60%,#eef4f8 100%)}
  .ph-sanitizer{background:linear-gradient(180deg,#eceff1,#d3d8dc)}
  .ph-black{background:radial-gradient(circle,#2b2b2b,#141414 55%,#f1f1f1 100%)}
  .ph-white{background:radial-gradient(circle,#fafafa,#dcdcdc)}
  .ph-4520{background:radial-gradient(circle,#f4f4f4,#d8d8d8 70%,#b33b34 100%)}
  .ph-4530{background:radial-gradient(circle,#37b3c2,#1f8f9e 70%,#eef2f2 100%)}
  .ph-bio{background:radial-gradient(circle,#e4302c,#b8201e 70%,#f4e4e2 100%)}
  .ph-wipes{background:linear-gradient(180deg,#f4f6f8,#c9d8e6)}
  .ph-spray{background:linear-gradient(180deg,#f0c93a 0,#f0c93a 20%,#f4f6f8 20%,#d5dfe9 100%)}

  /* ---------- back ---------- */
  .back-layout{width:100%;height:100%;display:flex;gap:14px}
  .back-products{width:330px;border:1.5px solid var(--green);display:flex;flex-direction:column}
  .back-mail{flex:1;position:relative}
  .stamp-box{position:absolute;top:0;right:0;width:64px;height:76px;border:1.5px solid var(--rule)}
  .return-address{position:absolute;top:78px;left:0;display:flex;gap:8px;align-items:flex-start}
  .return-address .brand-dot{width:20px;height:20px}
  .return-address .brand-name{font-size:14px}
  .return-address .brand-sub{font-size:5px;letter-spacing:1.6px}
  .return-address address{font-style:normal;font-size:7.5px;line-height:1.35;margin-left:4px}
  .address-lines{position:absolute;left:0;right:0;top:170px}
  .address-line{height:1px;background:var(--rule);margin-bottom:30px}
</style>
</head>
<body>

<article class="postcard postcard--front">
  <div class="front-frame">
    <div class="front-body">
      <section class="intro">
        <div class="brand">
          <span class="brand-dot"></span>
          <div>
            <div class="brand-name">CAREVALE</div>
            <div class="brand-sub">MEDICAL SUPPLY</div>
          </div>
        </div>
        <h1 class="headline">CAREVALE IS HERE <span>FOR YOU!</span></h1>
        <p class="intro-copy">Supplies available nationwide from Hawai‘i to New York &amp; everywhere in between.</p>
        <div class="promo">
          <div class="promo-code">PROMO CODE<strong>10OFF</strong></div>
          <div class="promo-offer"><span class="for">FOR</span><span class="pct">10%</span><span class="off">OFF</span></div>
        </div>
      </section>

      <section class="product-grid">
        <div class="product"><div class="product-photo ph-shield" role="img" aria-label="Clear face shield with headband"></div><div class="product-label">FACE SHIELDS</div></div>
        <div class="product"><div class="product-photo ph-nitrile" role="img" aria-label="Hands in blue nitrile gloves"></div><div class="product-label">NITRILE GLOVES</div></div>
        <div class="product"><div class="product-photo ph-vinyl" role="img" aria-label="Hand in clear vinyl glove"></div><div class="product-label">VINYL GLOVES</div></div>
        <div class="product"><div class="product-photo ph-gown" role="img" aria-label="Blue isolation gown with detail circles"></div><div class="product-label">ISOLATION GOWNS</div></div>
        <div class="product"><div class="product-photo ph-sanitizer" role="img" aria-label="Three gallon jugs of hand sanitizer"></div><div class="product-label">GALLON HAND SANITIZER</div></div>
        <div class="product"><div class="product-photo ph-black" role="img" aria-label="Black KN95 mask"></div><div class="product-label">BLACK KN95'S</div></div>
      </section>
    </div>

    <footer class="contact-bar">
      <span class="contact-item"><span class="contact-icon"><svg width="8" height="8" viewBox="0 0 24 24"><path fill="#fff" d="M6.6 10.8a15 15 0 0 0 6.6 6.6l2.2-2.2c.3-.3.7-.4 1-.2 1.1.4 2.3.6 3.6.6.6 0 1 .4 1 1V20c0 .6-.4 1-1 1A17 17 0 0 1 3 4c0-.6.4-1 1-1h3.5c.6 0 1 .4 1 1 0 1.3.2 2.5.6 3.6.1.3 0 .7-.2 1z"/></svg></span>808-241-7739</span>
      <span class="contact-item"><span class="contact-icon"><svg width="9" height="9" viewBox="0 0 24 24" fill="none" stroke="#fff" stroke-width="2"><circle cx="12" cy="12" r="9"/><path d="M3 12h18M12 3c3 3 3 15 0 18M12 3c-3 3-3 15 0 18"/></svg></span>www.carevale.shop</span>
    </footer>
  </div>
</article>

<article class="postcard postcard--back">
  <div class="back-layout">
    <div class="back-products">
      <section class="product-grid product-grid--back">
        <div class="product"><div class="product-photo ph-white" role="img" aria-label="White KN95 mask"></div><div class="product-label">WHITE KN95'S</div></div>
        <div class="product"><div class="product-photo ph-4520" role="img" aria-label="White folded N95 respirator with red straps"></div><div class="product-label">4520 N95</div></div>
        <div class="product"><div class="product-photo ph-4530" role="img" aria-label="Teal cup-style N95 respirator"></div><div class="product-label">4530 N95</div></div>
        <div class="product"><div class="product-photo ph-bio" role="img" aria-label="Red biohazard bags"></div><div class="product-label">BIOHAZARD BAGS</div></div>
        <div class="product"><div class="product-photo ph-wipes" role="img" aria-label="Canister of disinfecting wipes"></div><div class="product-label">PURATEX WIPES</div></div>
        <div class="product"><div class="product-photo ph-spray" role="img" aria-label="Spray bottle with yellow trigger"></div><div class="product-label">KOR SPRAY</div></div>
      </section>
      <footer class="contact-bar" style="gap:12px;font-size:9px">
        <span class="contact-item"><span class="contact-icon"><svg width="8" height="8" viewBox="0 0 24 24"><path fill="#fff" d="M6.6 10.8a15 15 0 0 0 6.6 6.6l2.2-2.2c.3-.3.7-.4 1-.2 1.1.4 2.3.6 3.6.6.6 0 1 .4 1 1V20c0 .6-.4 1-1 1A17 17 0 0 1 3 4c0-.6.4-1 1-1h3.5c.6 0 1 .4 1 1 0 1.3.2 2.5.6 3.6.1.3 0 .7-.2 1z"/></svg></span>808-241-7739</span>
        <span class="contact-item"><span class="contact-icon"><svg width="8" height="8" viewBox="0 0 24 24" fill="none" stroke="#fff" stroke-width="2.4"><rect x="3" y="5" width="18" height="14"/><path d="M3 6l9 7 9-7"/></svg></span>info@carevale.shop</span>
        <span class="contact-item"><span class="contact-icon"><svg width="9" height="9" viewBox="0 0 24 24" fill="none" stroke="#fff" stroke-width="2"><circle cx="12" cy="12" r="9"/><path d="M3 12h18M12 3c3 3 3 15 0 18M12 3c-3 3-3 15 0 18"/></svg></span>www.carevale.shop</span>
      </footer>
    </div>

    <section class="back-mail">
      <div class="stamp-box"></div>
      <div class="return-address">
        <span class="brand-dot"></span>
        <div>
          <div class="brand-name">CAREVALE</div>
          <div class="brand-sub">MEDICAL SUPPLY</div>
        </div>
        <address>P.O. Box 4172<br>Honolulu, HI 96812</address>
      </div>
      <div class="address-lines">
        <div class="address-line"></div>
        <div class="address-line"></div>
        <div class="address-line"></div>
      </div>
    </section>
  </div>
</article>

</body>
</html>
```